tovrin company need business card, envelope and letterhead design

Check on the attached file wherein you can find our logo and information about the company
Business card will double sided English version and Arabic version

Industry/Entity Type

Business

Requirements
Must have
• include the design also for the letterhead and envelop
Nice to have

```html
<!DOCTYPE html>
<html lang="en">
<head>
<meta charset="utf-8">
<title>Tovrin – Business Card</title>
<link rel="stylesheet" href="https://fonts.googleapis.com/css2?family=Roboto:wght@300;400;500;700&family=Cairo:wght@700&display=swap">
<style>
  :root {
    --page-bg: #ebe7e1;
    --card-bg: #f7f5f2;
    --card-edge: #dedad4;
    --brand-blue: #2a86c2;
    --text-grey: #8e8e8e;
    --label-grey: #9c9c9c;
  }
  * { margin: 0; padding: 0; box-sizing: border-box; }
  html, body {
    width: 1200px;
    height: 1047px;
    overflow: hidden;
    background: var(--page-bg);
    font-family: "Roboto", Arial, sans-serif;
  }
  .business-card {
    position: absolute;
    left: 151px;
    top: 291px;
    width: 946px;
    height: 516px;
    background: var(--card-bg);
    border: 1px solid var(--card-edge);
    border-radius: 16px;
    box-shadow: 0 10px 30px rgba(0,0,0,0.08);
  }
  .brand {
    position: absolute;
    left: 46px;
    top: 52px;
    width: 340px;
  }
  .brand-row {
    display: flex;
    align-items: center;
    gap: 16px;
  }
  .brand-square {
    width: 40px;
    height: 40px;
    background: var(--brand-blue);
  }
  .brand-name {
    font-weight: 700;
    font-size: 44px;
    letter-spacing: 3px;
    color: var(--brand-blue);
    line-height: 1;
  }
  .brand-name-arabic {
    margin-top: 2px;
    padding-left: 150px;
    font-family: "Cairo", "Roboto", sans-serif;
    font-weight: 700;
    font-size: 30px;
    line-height: 1.2;
    color: var(--brand-blue);
  }
  .holder-name {
    position: absolute;
    left: 46px;
    top: 225px;
    font-size: 26px;
    font-weight: 500;
    line-height: 32px;
    color: var(--brand-blue);
  }
  .holder-title {
    position: absolute;
    left: 46px;
    top: 258px;
    font-size: 21px;
    font-weight: 300;
    line-height: 28px;
    color: var(--label-grey);
  }
  .holder-mobile {
    position: absolute;
    left: 46px;
    top: 285px;
    font-size: 22px;
    font-weight: 500;
    line-height: 28px;
    letter-spacing: 0.5px;
    color: var(--brand-blue);
  }
  .contact-list {
    position: absolute;
    left: 46px;
    top: 326px;
    list-style: none;
  }
  .contact-item {
    display: flex;
    align-items: center;
    height: 29px;
    font-size: 21px;
    font-weight: 300;
    color: var(--text-grey);
  }
  .contact-icon {
    width: 16px;
    height: 16px;
    margin-right: 16px;
    fill: var(--brand-blue);
  }
  .address {
    position: absolute;
    left: 46px;
    top: 422px;
    font-size: 21px;
    font-weight: 300;
    line-height: 28px;
    color: var(--label-grey);
    font-style: normal;
  }
  .brand-feature {
    position: absolute;
    left: 486px;
    top: 200px;
    width: 458px;
    text-align: center;
    font-weight: 700;
    font-size: 100px;
    letter-spacing: 4px;
    color: var(--brand-blue);
    line-height: 1;
  }
</style>
</head>
<body>
  <div class="business-card">
    <div class="brand">
      <div class="brand-row">
        <div class="brand-square"></div>
        <div class="brand-name">TOVRIN</div>
      </div>
      <div class="brand-name-arabic" lang="ar" dir="rtl">توفرين</div>
    </div>

    <div class="holder-name">Faris Bin Omar Al Nadeem</div>
    <div class="holder-title">General Manager</div>
    <div class="holder-mobile">+966 555 318 402</div>

    <ul class="contact-list">
      <li class="contact-item">
        <svg class="contact-icon" viewBox="0 0 24 24" aria-hidden="true"><path d="M6.6 10.8c1.4 2.8 3.8 5.1 6.6 6.6l2.2-2.2c.3-.3.7-.4 1-.2 1.1.4 2.3.6 3.6.6.6 0 1 .4 1 1V20c0 .6-.4 1-1 1C10.6 21 3 13.4 3 4c0-.6.4-1 1-1h3.5c.6 0 1 .4 1 1 0 1.3.2 2.5.6 3.6.1.3 0 .7-.2 1L6.6 10.8z"/></svg>
        011 4720356
      </li>
      <li class="contact-item">
        <svg class="contact-icon" viewBox="0 0 24 24" aria-hidden="true"><path d="M7 3h10v5H7zM4 9h16a2 2 0 0 1 2 2v6h-4v4H6v-4H2v-6a2 2 0 0 1 2-2zm4 7v3h8v-3z"/></svg>
        011 4720 357
      </li>
      <li class="contact-item">
        <svg class="contact-icon" viewBox="0 0 24 24" aria-hidden="true"><path d="M3 5h18v14H3zm2 2v.5l7 5 7-5V7zm0 3v7h14v-7l-7 5z"/></svg>
        tovrin.sa@mailbox.com
      </li>
    </ul>

    <address class="address">
      Qasr Garden Road<br>
      Al Nakheel- P.O. Box 5214-13381
    </address>

    <div class="brand-feature">TOVRIN</div>
  </div>
</body>
</html>
```